Design some Business Cards for ROP Studio

Redesign our business cards for ROP, We had some business cards designed but we dont like the style and dont think they are professional enough please can you redesign them thanks

```html
<!DOCTYPE html>
<html lang="en">
<head>
<meta charset="utf-8">
<title>ROP Business Cards</title>
<link href="https://fonts.googleapis.com/css2?family=Raleway:wght@300;400;500&display=swap" rel="stylesheet">
<style>
  :root {
    --backdrop: #ecebe9;
    --card-black: #111111;
    --card-charcoal: #242424;
    --strip-grey: #3b3b3b;
    --ink-white: #f2f2f2;
    --ink-soft: #bdbdbd;
  }
  * { margin: 0; padding: 0; box-sizing: border-box; }
  html, body {
    width: 1200px; height: 960px; overflow: hidden;
    background: var(--backdrop);
    font-family: "Raleway", sans-serif;
  }
  .sheet {
    position: relative; width: 1200px; height: 960px;
    display: flex; flex-direction: column; align-items: center; justify-content: center;
    gap: 60px;
  }
  .card {
    position: relative; width: 700px; height: 400px;
    background: var(--card-black);
    color: var(--ink-white);
    display: flex; overflow: hidden;
    box-shadow: 0 6px 18px rgba(0,0,0,0.18);
  }
  .card__strip {
    width: 58px; height: 100%;
    background: var(--strip-grey);
    display: flex; align-items: center; justify-content: center;
  }
  .card__web {
    transform: rotate(-90deg);
    white-space: nowrap;
    font-size: 15px; font-weight: 400; letter-spacing: 1.5px;
    color: var(--ink-soft);
  }
  .card__face { position: relative; flex: 1; height: 100%; }
  .card__texture {
    position: absolute; inset: 0;
    background: linear-gradient(135deg, #0e0e0e 0%, var(--card-charcoal) 45%, #151515 70%, #0b0b0b 100%);
  }
  .card__links {
    position: absolute; top: 30px; right: 34px;
    text-align: right; font-size: 15px; font-weight: 400; line-height: 1.45;
    color: var(--ink-white);
  }
  .card__brand {
    position: absolute; left: 56px; top: 165px;
  }
  .card__name {
    font-size: 44px; font-weight: 300; letter-spacing: 3px;
    color: var(--ink-white); white-space: nowrap;
  }
  .card__tagline {
    margin-top: 8px; font-size: 13px; font-weight: 300; letter-spacing: 1px;
    color: var(--ink-soft);
  }
  .card__contact {
    position: absolute; right: 34px; bottom: 40px;
    text-align: right; font-size: 19px; font-weight: 400; line-height: 1.4;
  }
</style>
</head>
<body>
<main class="sheet">

  <article class="card card--foundation">
    <div class="card__strip"><span class="card__web">www.ropfoundation.org.uk</span></div>
    <div class="card__face">
      <div class="card__texture" role="img" aria-label="Dark faceted polygon background pattern"></div>
      <div class="card__links">
        <p>news.ropfoundation.org.uk</p>
        <p>events.ropfoundation.org.uk</p>
        <p>gallery.ropfoundation.org.uk</p>
      </div>
      <div class="card__brand">
        <p class="card__name">ROP Foundation</p>
        <p class="card__tagline">Build Bold Every Day</p>
      </div>
      <div class="card__contact">
        <p>Dario Menteith</p>
        <p>+44 7700 900314</p>
        <p>dario@ropfoundation.org.uk</p>
      </div>
    </div>
  </article>

  <article class="card card--studio">
    <div class="card__strip"><span class="card__web">www.ropstudio.com</span></div>
    <div class="card__face">
      <div class="card__texture" role="img" aria-label="Dark faceted polygon background pattern"></div>
      <div class="card__links">
        <p>news.ropstudio.com</p>
        <p>events.ropstudio.com</p>
        <p>gallery.ropstudio.com</p>
      </div>
      <div class="card__brand">
        <p class="card__name">ROP Studio</p>
        <p class="card__tagline">Shape What Is Next</p>
      </div>
      <div class="card__contact">
        <p>Dario Menteith</p>
        <p>+44 7700 900314</p>
        <p>dario@ropstudio.com</p>
      </div>
    </div>
  </article>

</main>
</body>
</html>
```